Whole Body Cryotherapy Brochure Design Project

We need a tri-fold brochure design for our new Whole Body Cryotherapy chamber in San Antonio, TX. The WBC chamber is the first available to the public in the area. WBC has many benefits including, but not limited to reduce swelling & inflammation, whole body recovery, pain relief, sports enhancement, anti-aging & metabolic boost. We created an "unprofessional" brochure with as much information as we could possibly fit. This "professional" brochure should be eye catching, clean & modern & simple. We would also like the brochure to have pricing & Introductory coupon. We've attached the "unprofessional" brochure we created & also the window sign & poster we had "professionally" created along with our logo (blue & black; either layout).

Requirements
Must have
• Princing:
Single Session $75
3 Session Package $195
6 Session Package $360
9 Session Package $495
12 Session Package $600
Discounts for Merrow Motion & Joint patients, Ironloop, members of the military & service personnel.
Packages can be shared.
Payment plans are available.
Large Group discounts are also available.

Coupon:
Introductory Session (for new WBC clients only)
$45 (Regular Price $75)

```html
<!DOCTYPE html>
<html lang="en">
<head>
<meta charset="utf-8">
<title>Whole Body Cryotherapy Brochure</title>
<link href="https://fonts.googleapis.com/css2?family=Oswald:wght@400;600;700&family=Open+Sans:wght@400;600;700&display=swap" rel="stylesheet">
<style>
  :root{
    --blue:#1b8fd8;
    --blue-deep:#136fae;
    --ink:#111416;
    --charcoal:#3a3d40;
    --paper:#ffffff;
    --backdrop:#e6e7e9;
    --steel-1:#4b5560;
    --steel-2:#1c242c;
    --rule:rgba(255,255,255,.18);
  }
  *{box-sizing:border-box;margin:0;padding:0}
  html,body{width:1200px;height:838px;overflow:hidden}
  body{background:var(--backdrop);font-family:"Open Sans",Arial,sans-serif;display:flex;align-items:center;justify-content:center}
  .brochure{width:1080px;height:760px;display:flex;box-shadow:0 6px 24px rgba(0,0,0,.18)}
  .panel{width:360px;height:760px;position:relative;overflow:hidden}

  /* Inside panel */
  .panel--info{background:var(--blue);color:var(--paper);padding:28px 30px}
  .info-photo{height:170px;background:linear-gradient(160deg,#cfd4d8,#6e767d 60%,#2f353a);border:3px solid rgba(255,255,255,.35)}
  .section-title{font-family:"Oswald",Arial,sans-serif;font-weight:600;font-size:21px;line-height:1.15;text-transform:uppercase;letter-spacing:.5px;display:flex;gap:10px;align-items:flex-start;margin:22px 0 14px}
  .section-title svg{flex:none;margin-top:5px}
  .info-text{font-size:11.5px;line-height:1.65;text-align:justify}
  .applications{list-style:none;font-size:13px;line-height:1.6;letter-spacing:2px;text-transform:uppercase;padding-left:26px}

  /* Back panel */
  .panel--contact{background:var(--ink);color:var(--paper);display:flex;flex-direction:column}
  .contact-photo{height:250px;flex:none;background:linear-gradient(170deg,#8d98a2 0%,var(--steel-1) 45%,var(--steel-2) 100%)}
  .pricing{padding:16px 26px 0}
  .pricing-title{font-family:"Oswald",Arial,sans-serif;font-weight:600;font-size:17px;letter-spacing:1px;text-transform:uppercase;color:var(--blue);margin-bottom:6px}
  .price-list{list-style:none;font-size:12px}
  .price-list li{display:flex;justify-content:space-between;padding:3px 0;border-bottom:1px solid var(--rule)}
  .price-list strong{font-family:"Oswald",Arial,sans-serif;font-weight:600;font-size:13px}
  .price-notes{list-style:none;font-size:9.5px;line-height:1.5;margin-top:7px;opacity:.9}
  .coupon{margin:12px 26px 0;border:2px dashed var(--blue);padding:8px 12px;display:flex;justify-content:space-between;align-items:center}
  .coupon-label{font-size:10px;line-height:1.35;text-transform:uppercase;letter-spacing:.5px}
  .coupon-label b{display:block;font-family:"Oswald",Arial,sans-serif;font-weight:600;font-size:14px;letter-spacing:1px}
  .coupon-price{text-align:right;font-family:"Oswald",Arial,sans-serif;font-weight:700;font-size:30px;line-height:1;color:var(--blue)}
  .coupon-price small{display:block;font-family:"Open Sans",Arial,sans-serif;font-weight:400;font-size:9px;color:var(--paper);margin-top:3px}
  .contact-band{padding:14px 20px 0;text-align:center}
  .contact-cta{font-family:"Oswald",Arial,sans-serif;font-weight:600;font-size:15px;letter-spacing:.5px;text-transform:uppercase;white-space:nowrap}
  .contact-phone{font-family:"Oswald",Arial,sans-serif;font-size:21px;letter-spacing:2px;margin-top:2px}
  .brand{display:flex;align-items:center;justify-content:center;gap:10px;margin-top:12px}
  .brand-mark{width:20px;height:20px;background:var(--paper);flex:none}
  .brand-name{font-family:"Oswald",Arial,sans-serif;font-weight:400;font-size:16px;letter-spacing:1.5px;text-transform:uppercase;white-space:nowrap}

  /* Cover panel */
  .panel--cover{background:var(--paper)}
  .cover-title{font-family:"Oswald",Arial,sans-serif;font-weight:700;font-size:70px;line-height:.9;color:var(--charcoal);text-transform:uppercase;padding:34px 0 14px 40px}
  .cover-band{background:var(--blue);color:var(--paper);font-family:"Oswald",Arial,sans-serif;font-weight:600;font-size:36px;letter-spacing:1px;text-transform:uppercase;padding:4px 0 4px 40px}
  .benefits{display:flex;gap:26px;padding:14px 0 0 40px;font-size:10px;line-height:1.6;text-transform:uppercase;letter-spacing:.6px;color:var(--ink)}
  .benefits ul{list-style:none}
  .cover-footer{position:absolute;left:0;bottom:0;width:360px;height:330px}
  .cover-footer svg{position:absolute;inset:0}
  .chamber-photo{position:absolute;right:30px;top:360px;width:150px;height:180px;border-radius:60px 60px 8px 8px;background:linear-gradient(180deg,#f2f3f4,#9ba2a8 55%,#6b737a);z-index:2}
  .cover-web{position:absolute;left:0;bottom:0;width:60px;height:300px;background:var(--ink);color:var(--paper);display:flex;flex-direction:column;justify-content:flex-end;align-items:center;gap:16px;padding-bottom:18px}
  .cover-web span{writing-mode:vertical-rl;transform:rotate(180deg);font-size:10px;font-weight:600;letter-spacing:.4px;white-space:nowrap}
  .cover-brand{position:absolute;left:90px;bottom:168px;display:flex;align-items:center;gap:10px;color:var(--paper)}
  .cover-brand .brand-name{font-size:15px}
  .tagline{position:absolute;left:90px;bottom:36px;font-family:"Oswald",Arial,sans-serif;font-weight:700;font-size:30px;line-height:1.05;color:var(--paper);text-transform:uppercase}
</style>
</head>
<body>
  <main class="brochure">
    <section class="panel panel--info">
      <div class="info-photo" role="img" aria-label="Photo of the open top of a cryotherapy chamber"></div>
      <h2 class="section-title">
        <svg width="14" height="14" viewBox="0 0 14 14"><path d="M0 14L14 0V14Z" fill="#fff"/></svg>
        What is whole body cryotherapy?
      </h2>
      <p class="info-text">With Whole Body Cryotherapy (WBC) the body is exposed to ultra-low temperatures, triggering a systemic anti-inflammatory response. This therapy was first utilized in Japan in the early 1970s by Dr. Hallworth to treat rheumatoid arthritis. Studies conducted over the last two decades have verified WBC as a powerful treatment for inflammatory disorders and injuries. Professional athletes have discovered WBC as a powerful treatment to decrease recovery time, increase athletic performance, and boost the body's metabolic rate.</p>
      <h2 class="section-title">
        <svg width="14" height="14" viewBox="0 0 14 14"><path d="M0 14L14 0V14Z" fill="#fff"/></svg>
        Applications
      </h2>
      <ul class="applications">
        <li>Athletic performance</li>
        <li>Postsurgical recovery</li>
        <li>Musculoskeletal injuries</li>
        <li>Rheumatoid arthritis</li>
        <li>Weight management</li>
        <li>Skin disorders</li>
        <li>Autoimmune and other</li>
        <li>Inflammatory disorders</li>
      </ul>
    </section>

    <section class="panel panel--contact">
      <div class="contact-photo" role="img" aria-label="Photo of an athlete standing in a misting cryotherapy chamber"></div>
      <div class="pricing">
        <h3 class="pricing-title">Pricing</h3>
        <ul class="price-list">
          <li><span>Single Session</span><strong>$75</strong></li>
          <li><span>3 Session Package</span><strong>$195</strong></li>
          <li><span>6 Session Package</span><strong>$360</strong></li>
          <li><span>9 Session Package</span><strong>$495</strong></li>
          <li><span>12 Session Package</span><strong>$600</strong></li>
        </ul>
        <ul class="price-notes">
          <li>Discounts for Merrow Motion &amp; Joint patients, Ironloop, members of the military &amp; service personnel.</li>
          <li>Packages can be shared. Payment plans are available.</li>
          <li>Large group discounts are also available.</li>
        </ul>
      </div>
      <div class="coupon">
        <p class="coupon-label"><b>Introductory Session</b>For new WBC clients only</p>
        <p class="coupon-price">$45<small>Regular Price $75</small></p>
      </div>
      <div class="contact-band">
        <p class="contact-cta">Call to schedule an appointment today</p>
        <p class="contact-phone">210-555-0148</p>
        <div class="brand">
          <span class="brand-mark"></span>
          <span class="brand-name">Merrow Motion &amp; Joint</span>
        </div>
      </div>
    </section>

    <section class="panel panel--cover">
      <h1 class="cover-title">Whole<br>Body</h1>
      <div class="cover-band">Cryotherapy</div>
      <div class="benefits">
        <ul><li>Pain management</li><li>Injury therapy</li><li>Rapid recovery</li><li>Performance</li></ul>
        <ul><li>Metabolic boost</li><li>Immunity boost</li><li>Anti-aging</li><li>Skin rejuvenation</li></ul>
      </div>
      <div class="cover-footer">
        <svg width="360" height="330" viewBox="0 0 360 330"><path d="M0 90L360 0V330H0Z" fill="var(--blue)"/><path d="M0 150L360 60V90L0 180Z" fill="var(--blue-deep)" opacity=".5"/></svg>
        <div class="cover-web"><span>www.merrowmotion.com</span><span>@merrowmotion</span></div>
        <div class="cover-brand"><span class="brand-mark"></span><span class="brand-name">Merrow Motion &amp; Joint</span></div>
        <p class="tagline">Just 3<br>minutes<br>for whole<br>body recovery</p>
      </div>
      <div class="chamber-photo" role="img" aria-label="Product photo of the cryotherapy chamber"></div>
    </section>
  </main>
</body>
</html>
```